Need a new office flyer

I would like an 8.5 x 11" flyer made that can be emailed or printed out and handed to potential customers.  The flyer should include our existing logo and continuity of branding.   I am a commercial real estate broker and market myself to business with 5-50 employee's that are looking to buy or lease space to run their business from.  I focus my efforts on office & warehouse space. The flyer should have a banner "need a new location "
"VLD commercial real estate specializes in helping business and professionals buy/sell or lease  the best spaces for their business.  Take the stress & time out of finding the best location for your business and negotiating a great deal  VLD will do it for you and the best part our service is free to you. Working with VLD is easy as 1, 2, 3
1. Call, Text, Email us today and let us know what your looking to do.
2. VLD  will prepare a list of all the best available spaces that meet your specifications and set up tours of your favorites.
3. We will negotiate the best terms for your space. and help you with all the  details of getting your new space ready for you.
Don't forget the that our services are free to Buyers and Tenants so don't waste your companies time searching for locations, we already know where they are!
Contact us today!
Dale Norcutt
DRE 07354128
VLD Commercial Real Estate
555-317-4829
d.norcutt@vldprop-example.com

```html
<!DOCTYPE html>
<html lang="en">
<head>
<meta charset="UTF-8">
<title>VLD Commercial Real Estate – Need a New Location</title>
<link rel="stylesheet" href="https://fonts.googleapis.com/css2?family=Montserrat:wght@400;500;600;800&display=swap">
<style>
  :root {
    --page-bg: #b9b9bb;
    --paper: #f3f5f7;
    --brand-blue: #1f5e9a;
    --accent-blue: #2b78b8;
    --body-grey: #5e6166;
    --contact-soft: #b9cfe4;
    --white: #ffffff;
  }
  * { margin: 0; padding: 0; box-sizing: border-box; }
  html, body { width: 1200px; height: 960px; overflow: hidden; }
  body {
    background: var(--page-bg);
    font-family: "Montserrat", Arial, sans-serif;
    position: relative;
  }
  .flyer {
    position: absolute;
    left: 250px; top: 27px;
    width: 700px; height: 906px;
    background: var(--paper);
    overflow: hidden;
    box-shadow: 0 6px 24px rgba(0,0,0,.18);
  }
  .flyer-backdrop {
    position: absolute; inset: 0;
    background: linear-gradient(100deg, #c9cccf 0%, #dfe2e5 9%, #eef0f2 16%, #f5f6f8 55%, #e7eaec 100%);
  }
  .flyer-graphics { position: absolute; inset: 0; }
  .brand {
    position: absolute; left: 42px; top: 38px;
    display: flex; align-items: center; gap: 8px;
    color: var(--brand-blue);
    font-weight: 800; font-size: 28px; letter-spacing: 1px;
  }
  .brand-dot {
    width: 24px; height: 24px; border-radius: 50%;
    background: var(--brand-blue);
  }
  .headline {
    position: absolute; left: 40px; top: 88px;
    color: var(--brand-blue);
    font-weight: 800; font-size: 60px; line-height: .98;
    letter-spacing: 1px;
  }
  .copy {
    position: absolute; left: 42px; top: 234px; width: 300px;
    color: var(--body-grey);
    font-weight: 500; font-size: 12.5px; line-height: 1.36;
  }
  .copy p { margin-bottom: 10px; }
  .copy .step { margin-bottom: 8px; }
  .copy .lead, .copy .closing { color: var(--accent-blue); font-weight: 600; }
  .copy .lead { margin-bottom: 2px; }
  .copy .closing { margin-top: 12px; margin-bottom: 0; }
  .step-num { color: var(--accent-blue); font-weight: 600; }
  .contact {
    position: absolute; left: 42px; top: 712px;
    color: var(--white); font-size: 16px; line-height: 1.45; font-weight: 500;
  }
  .contact-title { color: var(--contact-soft); font-weight: 400; letter-spacing: 1px; margin-bottom: 8px; }
  .reach {
    position: absolute; left: 290px; top: 836px;
    color: var(--white); font-size: 18px; line-height: 1.4; font-weight: 500;
  }
</style>
</head>
<body>
  <main class="flyer">
    <div class="flyer-backdrop" role="img" aria-label="Faint photograph of a bright office interior"></div>

    <svg class="flyer-graphics" width="700" height="906" viewBox="0 0 700 906">
      <defs>
        <linearGradient id="office-photo" x1="0" y1="0" x2="1" y2="1">
          <stop offset="0" stop-color="#d9c9a4"/>
          <stop offset=".45" stop-color="#aeb59c"/>
          <stop offset="1" stop-color="#5f6860"/>
        </linearGradient>
        <linearGradient id="contact-band" x1="0" y1="0" x2="0" y2="1">
          <stop offset="0" stop-color="#2d74b0"/>
          <stop offset="1" stop-color="#255d92"/>
        </linearGradient>
        <clipPath id="circle-clip"><circle cx="640" cy="640" r="250"/></clipPath>
      </defs>
      <circle cx="640" cy="640" r="274" fill="#2b6ca8"/>
      <circle cx="640" cy="640" r="262" fill="#a9aeb3"/>
      <g role="img" aria-label="Photograph of a glass-walled office with carpeted floor">
        <rect x="380" y="380" width="520" height="520" fill="url(#office-photo)" clip-path="url(#circle-clip)"/>
      </g>
      <rect x="0" y="692" width="700" height="214" fill="url(#contact-band)" opacity=".93"/>
    </svg>

    <div class="brand"><span class="brand-dot"></span>VLD</div>

    <h1 class="headline">NEED A NEW<br>LOCATION</h1>

    <section class="copy">
      <p>VLD commercial real estate specializes in helping business and professionals buy/sell or lease the best spaces for their business. Take the stress &amp; time out of finding the best location for your business and negotiating a great deal VLD will do it for you and the best part our service is free to you.</p>
      <p class="lead">Working with VLD is easy as 1, 2, 3</p>
      <p class="step"><span class="step-num">1.</span> Call, Text, Email us today and let us know what your looking to do.</p>
      <p class="step"><span class="step-num">2.</span> VLD will prepare a list of all the best available spaces that meet your specifications and set up tours of your favorites.</p>
      <p class="step"><span class="step-num">3.</span> We will negotiate the best terms for your space. and help you with all the details of getting your new space ready for you.</p>
      <p class="closing">Don't forget the that our services are free to Buyers and Tenants so don't waste your companies time searching for locations, we already know where they are!</p>
    </section>

    <section class="contact">
      <p class="contact-title">CONTACT US TODAY!</p>
      <p>Dale Norcutt</p>
      <p>DRE 07354128</p>
      <p>VLD Commercial Real Estate</p>
    </section>

    <section class="reach">
      <p>555-317-4829</p>
      <p>d.norcutt@vldprop-example.com</p>
    </section>
  </main>
</body>
</html>
```